Kestrel Bridge Consulting (KBC) Business Card Design

I would like to create double-sided business cards that contain:
1) Name: Derek Molvane
2) Phone Number: +1 (555) 218-4907
3) Email: Derek.Molvane@KestrelBridgeConsulting.example
4) Website: KestrelBridgeConsulting.example

I would like to include my logo and a color scheme similar to the Varnholt Grand Prix Ostera squad color scheme (black, silver, greenish-blue – but can also include regular blue)

What we do: Our company develops and delivers innovative and pragmatic information technology and cybersecurity risk and compliance solutions for organizations in the commercial market as well as the federal, and state/local sectors.

```html
<!DOCTYPE html>
<html lang="en">
<head>
<meta charset="UTF-8">
<title>Kestrel Bridge Consulting — Business Card</title>
<link rel="stylesheet" href="https://fonts.googleapis.com/css2?family=Montserrat:wght@500;600&family=Roboto+Condensed:wght@400&display=swap">
<style>
  :root {
    --stage: #3a3a3c;
    --paper: #ffffff;
    --navy-deep: #050c22;
    --navy: #0b1c3d;
    --navy-glow: #123a6b;
    --brand-blue: #1a9be8;
    --brand-cyan: #25c3f0;
    --ink-dark: #14161c;
    --ink-light: #ffffff;
    --rule: #6b7890;
  }
  * { box-sizing: border-box; margin: 0; padding: 0; }
  html, body {
    width: 1200px; height: 1200px; overflow: hidden;
    background: var(--stage);
  }
  .sheet {
    position: relative; width: 1200px; height: 1200px;
    display: flex; flex-direction: column; align-items: center;
    justify-content: center; gap: 60px;
  }
  .card {
    position: relative; width: 900px; height: 514px;
    border-radius: 28px; overflow: hidden;
    box-shadow: 0 18px 40px rgba(0,0,0,.45);
  }

  /* ---------- front ---------- */
  .card--front { background: var(--paper); }
  .front__top {
    position: absolute; left: 0; top: 0; width: 100%; height: 282px;
    display: flex; align-items: center; justify-content: center;
    padding-right: 120px;
  }
  .front__accent {
    position: absolute; left: 0; top: 282px; width: 100%; height: 9px;
    background: linear-gradient(90deg, var(--brand-blue), var(--brand-cyan));
  }
  .front__base {
    position: absolute; left: 0; top: 302px; width: 100%; height: 212px;
    background: linear-gradient(90deg, var(--navy-deep) 0%, var(--navy) 70%, var(--navy-glow) 100%);
  }
  .front__network {
    position: absolute; right: 0; top: 0; width: 60%; height: 100%;
    background: radial-gradient(ellipse at 75% 30%, rgba(40,120,190,.35), rgba(11,28,61,0) 70%);
  }
  .holder-name {
    position: absolute; left: 56px; top: 122px;
    font-family: "Montserrat", sans-serif; font-weight: 600;
    font-size: 34px; letter-spacing: 0.3px; color: var(--brand-blue);
    white-space: nowrap;
  }
  .front__divider {
    position: absolute; left: 410px; top: 44px; width: 1px; height: 118px;
    background: var(--rule);
  }
  .contact-list {
    position: absolute; left: 432px; top: 42px;
    list-style: none; display: flex; flex-direction: column; gap: 16px;
  }
  .contact-list li {
    display: flex; align-items: center; gap: 10px;
    font-family: "Roboto Condensed", sans-serif; font-size: 16px;
    color: var(--ink-light); text-transform: uppercase; white-space: nowrap;
  }
  .contact-list svg { width: 20px; height: 20px; flex: none; }

  /* ---------- lockup ---------- */
  .lockup { display: flex; align-items: center; gap: 26px; }
  .lockup__dot {
    width: 92px; height: 92px; border-radius: 50%;
    background: var(--brand-blue); flex: none;
  }
  .lockup__name {
    font-family: "Montserrat", sans-serif; font-weight: 500;
    font-size: 34px; line-height: 1.05; letter-spacing: 3px;
    text-transform: uppercase; color: var(--ink-dark);
  }
  .lockup__name span { display: block; }

  /* ---------- back ---------- */
  .card--back {
    background: linear-gradient(100deg, var(--navy-deep) 0%, var(--navy) 55%, var(--navy-glow) 100%);
    display: flex; align-items: center; justify-content: center;
  }
  .back__network {
    position: absolute; right: 0; top: 0; width: 65%; height: 100%;
    background: radial-gradient(ellipse at 60% 55%, rgba(50,140,210,.35), rgba(11,28,61,0) 70%);
  }
  .card--back .lockup { position: relative; }
  .card--back .lockup__dot { width: 120px; height: 120px; }
  .card--back .lockup__name { color: var(--ink-light); font-size: 44px; }
</style>
</head>
<body>
<main class="sheet">

  <section class="card card--front" aria-label="Business card front">
    <div class="front__top">
      <div class="lockup">
        <div class="lockup__dot"></div>
        <div class="lockup__name">
          <span>Kestrel</span><span>Bridge</span><span>Consulting</span>
        </div>
      </div>
    </div>
    <div class="front__accent"></div>
    <div class="front__base">
      <div class="front__network" role="img" aria-label="Faint hexagonal network pattern in blue"></div>
      <div class="front__divider"></div>
      <ul class="contact-list">
        <li>
          <svg viewBox="0 0 24 24"><path fill="#1a9be8" d="M6.6 10.8a15.1 15.1 0 0 0 6.6 6.6l2.2-2.2a1 1 0 0 1 1-.25 11.4 11.4 0 0 0 3.6.57 1 1 0 0 1 1 1V20a1 1 0 0 1-1 1A17 17 0 0 1 3 4a1 1 0 0 1 1-1h3.5a1 1 0 0 1 1 1c0 1.25.2 2.45.57 3.570a1 1 0 0 1-.25 1z"/></svg>
          +1 (555) 218-4907
        </li>
        <li>
          <svg viewBox="0 0 24 24" fill="none" stroke="#1a9be8" stroke-width="1.6"><circle cx="12" cy="12" r="9"/><ellipse cx="12" cy="12" rx="4" ry="9"/><path d="M3 12h18M5 7h14M5 17h14"/></svg>
          KestrelBridgeConsulting.example
        </li>
        <li>
          <svg viewBox="0 0 24 24"><path fill="#1a9be8" d="M2 5h20v14H2z"/><path fill="none" stroke="#0b1c3d" stroke-width="1.6" d="M2 5l10 8 10-8"/></svg>
          Derek.Molvane@KestrelBridgeConsulting.example
        </li>
      </ul>
      <p class="holder-name">DEREK MOLVANE</p>
    </div>
  </section>

  <section class="card card--back" aria-label="Business card back">
    <div class="back__network" role="img" aria-label="Faint hexagonal network pattern in blue"></div>
    <div class="lockup">
      <div class="lockup__dot"></div>
      <div class="lockup__name">
        <span>Kestrel</span><span>Bridge</span><span>Consulting</span>
      </div>
    </div>
  </section>

</main>
</body>
</html>
```